Plakat-Design für mobile Energiespeicher
Zielgruppe
Wir vertreiben mobile Energiespeicher und benötigen für unser Produkt einen Eyecatcher, der auf das Produkt aufmerksam macht. Unsere Zielgruppe sind erwachsene Personen.
Aufgabenstellung
Das Plakat ist für einen Kundenstopper bestimmt und sollte DIN-A0/DIN-A1-Größe haben. Wichtig ist, dass es ein Eyecatcher ist. Es kann sich um ein modernes Design handeln. Vielleicht ein knackiger Slogan? Auf dem Plakat selbst sollten nur wenige technische Details stehen. Dafür wird es separates Info-Material geben.

```html
<!DOCTYPE html>
<html lang="de">
<head>
<meta charset="utf-8">
<title>Voltaris – Power to go</title>
<link rel="stylesheet" href="https://fonts.googleapis.com/css2?family=Audiowide&family=Roboto:wght@400;500&display=swap">
<style>
  :root {
    --green: #9bc223;
    --green-dark: #8db71f;
    --green-light: #b4d35f;
    --white: #ffffff;
    --brand: #8fbf1c;
    --device-dark: #3a3b3d;
    --device-mid: #55575a;
  }
  * { margin: 0; padding: 0; box-sizing: border-box; }
  html, body { width: 848px; height: 1200px; overflow: hidden; background: var(--white); }
  .poster {
    position: relative;
    width: 848px;
    height: 1200px;
    background: var(--green);
    overflow: hidden;
  }
  .header {
    position: absolute;
    inset: 0 0 auto 0;
    height: 140px;
    background: var(--white);
  }
  .backdrop, .headline, .header-brand {
    position: absolute;
    left: 0;
    top: 0;
  }
  .brand-name {
    font-family: "Audiowide", sans-serif;
    fill: var(--brand);
  }
  .headline-text {
    font-family: "Audiowide", sans-serif;
    fill: var(--white);
  }
  .tagline {
    position: absolute;
    left: 0;
    width: 848px;
    top: 584px;
    text-align: center;
    font-family: "Roboto", sans-serif;
    font-weight: 400;
    color: var(--white);
    font-size: 37px;
    line-height: 52px;
    letter-spacing: 1.4px;
  }
  .product {
    position: absolute;
    left: 188px;
    top: 780px;
    width: 470px;
    height: 322px;
    border-radius: 28px 28px 22px 22px;
    background: linear-gradient(90deg, var(--device-dark) 0%, var(--device-mid) 55%, var(--device-dark) 82%, var(--green) 84%, #7fb515 100%);
  }
</style>
</head>
<body>
<main class="poster">
  <svg class="backdrop" width="848" height="1200" viewBox="0 0 848 1200" aria-hidden="true">
    <polygon points="0,834 424,1200 0,1200" fill="var(--green-dark)"/>
    <polygon points="848,978 848,1200 383,1200" fill="var(--green-light)"/>
  </svg>

  <header class="header">
    <svg class="header-brand" width="848" height="140" viewBox="0 0 848 140">
      <text class="brand-name" x="40" y="106" font-size="62" textLength="768" lengthAdjust="spacingAndGlyphs">VOLTARIS</text>
    </svg>
  </header>

  <svg class="headline" width="848" height="560" viewBox="0 0 848 560">
    <text class="headline-text" x="72" y="399" font-size="132" textLength="722" lengthAdjust="spacingAndGlyphs">POWER</text>
    <text class="headline-text" x="136" y="543" font-size="132" textLength="582" lengthAdjust="spacingAndGlyphs">TO GO</text>
  </svg>

  <p class="tagline">DEINE TRAGBARE STROMVERSORGUNG<br>UNABHÄNGIG VOM STROMNETZ</p>

  <div class="product" role="img" aria-label="Produktfoto: tragbare Powerstation in Dunkelgrau mit grüner Seitenwand, Display, USB-Anschlüssen und vier Steckdosen"></div>
</main>
</body>
</html>
```